VLO Nail Gel Polish Color Tip Swatch Label Design for SUN REEF collection

We need a label design for the color swatch that will go with our new collection of nail gel polish called SUN REEF. We are a nail and beauty supply distributor in the US selling to retail nail salons in the US only. Please also see our other project launched today: VLO Gel Nail Polish Collection for 15 ml bottle (Contest)

Target Market(s)

Retail Nail Salons in the US

Industry/Entity Type

Nail Salon

Font styles to use
Serif
Sans Serif

Colors

Designer to choose colors to be used in the design.

Requirements
Must have
• VLO Logo - this needs to be changed to all black color for letters VLO and matte gold drop for the "drop";
• SUN REEF in big font/easy to see;
• Numbers in big font/easy to see: CA1, CA2, .... CA16 on on side; and CA17, CA18, .... CA32 on the other side (as there will be 16 nail tips on each side).
• Label dimensions must be 1.875" x 9.0".
Nice to have
• possible additional wording, "Premium gel polish", "Collection"
Should not have
• no picture of SUN REEF; no overpowering graphics to make it look too busy

```html
<!DOCTYPE html>
<html lang="en">
<head>
<meta charset="utf-8">
<title>VLO Sun Reef Swatch Label</title>
<link rel="stylesheet" href="https://fonts.googleapis.com/css2?family=Cinzel:wght@400;700;900&family=Open+Sans:wght@400&display=swap">
<style>
  :root {
    --peach-light: #f6d6b8;
    --peach: #f1c4a6;
    --rose: #eaa793;
    --wave-blue: #5fc6f2;
    --wave-sky: #8fd6f6;
    --wave-lilac: #b9a6e6;
    --gold: #d4b041;
    --gold-dark: #9b7a1c;
    --ink: #1c1c1c;
    --label-ink: #3a2e2a;
  }
  * { margin: 0; padding: 0; box-sizing: border-box; }
  html, body { width: 1200px; height: 251px; overflow: hidden; }
  .swatch-label {
    position: relative;
    width: 1200px;
    height: 251px;
    overflow: hidden;
    background: linear-gradient(90deg,
      var(--peach) 0%, var(--rose) 9%, var(--peach-light) 20%, var(--rose) 32%,
      var(--peach-light) 45%, var(--rose) 58%, var(--peach-light) 70%,
      var(--rose) 82%, var(--peach-light) 92%, var(--rose) 100%);
  }
  .wave-band {
    position: absolute;
    left: 0; top: 60px;
    width: 1200px; height: 124px;
    background: linear-gradient(180deg,
      rgba(143,214,246,0.0) 0%, rgba(95,198,242,0.75) 18%,
      rgba(185,166,230,0.55) 50%, rgba(95,198,242,0.75) 80%,
      rgba(143,214,246,0.0) 100%);
  }
  .shade-numbers {
    position: absolute;
    left: 8px;
    width: 1171px;
    display: grid;
    grid-template-columns: repeat(16, 1fr);
  }
  .shade-numbers--top { top: 12px; height: 46px; align-items: end; }
  .shade-numbers--bottom { top: 190px; height: 46px; align-items: start; }
  .shade-number {
    justify-self: center;
    writing-mode: vertical-rl;
    transform: rotate(180deg);
    font-family: "Open Sans", sans-serif;
    font-size: 12px;
    letter-spacing: 0.5px;
    color: var(--label-ink);
  }
  .brand-mark {
    position: absolute;
    top: 80px;
    height: 86px;
    display: flex;
    align-items: center;
    justify-content: center;
    writing-mode: vertical-rl;
    font-family: "Cinzel", serif;
    font-weight: 700;
    font-size: 34px;
    color: var(--ink);
    line-height: 1;
  }
  .brand-mark--left { left: 34px; transform: rotate(180deg); }
  .brand-mark--right { left: 1128px; }
  .collection-title {
    position: absolute;
    left: 0; top: 70px;
    width: 1200px;
    text-align: center;
  }
  .collection-name {
    font-family: "Cinzel", serif;
    font-weight: 900;
    font-size: 94px;
    line-height: 1;
    letter-spacing: 6px;
    color: var(--gold);
    text-shadow: 2px 2px 2px rgba(120,90,20,0.55);
    padding-left: 40px;
  }
  .collection-tagline {
    margin-top: 4px;
    padding-left: 40px;
    font-family: "Cinzel", serif;
    font-weight: 400;
    font-size: 13px;
    letter-spacing: 11px;
    color: var(--ink);
    text-transform: uppercase;
  }
  .collection-tagline .initial { font-size: 19px; }
</style>
</head>
<body>
  <main class="swatch-label">
    <div class="wave-band" role="img" aria-label="Flowing blue and lilac silk ribbon waves across the middle of the label"></div>

    <div class="shade-numbers shade-numbers--top">
      <span class="shade-number">CA17</span><span class="shade-number">CA18</span>
      <span class="shade-number">CA19</span><span class="shade-number">CA20</span>
      <span class="shade-number">CA21</span><span class="shade-number">CA22</span>
      <span class="shade-number">CA23</span><span class="shade-number">CA24</span>
      <span class="shade-number">CA25</span><span class="shade-number">CA26</span>
      <span class="shade-number">CA27</span><span class="shade-number">CA28</span>
      <span class="shade-number">CA29</span><span class="shade-number">CA30</span>
      <span class="shade-number">CA31</span><span class="shade-number">CA32</span>
    </div>

    <div class="brand-mark brand-mark--left">VLO</div>
    <div class="brand-mark brand-mark--right">VLO</div>

    <div class="collection-title">
      <h1 class="collection-name">SUN REEF</h1>
      <p class="collection-tagline"><span class="initial">P</span>remium <span class="initial">G</span>el <span class="initial">P</span>olish</p>
    </div>

    <div class="shade-numbers shade-numbers--bottom">
      <span class="shade-number">CA1</span><span class="shade-number">CA2</span>
      <span class="shade-number">CA3</span><span class="shade-number">CA4</span>
      <span class="shade-number">CA5</span><span class="shade-number">CA6</span>
      <span class="shade-number">CA7</span><span class="shade-number">CA8</span>
      <span class="shade-number">CA9</span><span class="shade-number">CA10</span>
      <span class="shade-number">CA11</span><span class="shade-number">CA12</span>
      <span class="shade-number">CA13</span><span class="shade-number">CA14</span>
      <span class="shade-number">CA15</span><span class="shade-number">CA16</span>
    </div>
  </main>
</body>
</html>
```